TK Stationary Design

Logo, Business Card, Letterhead & Email Signature Design

Target Market(s)

Legal

Colors

Designer to choose colors to be used in the design.

Requirements
Must have
• Gold and Blue are the colours to use. The TK must be inside the Gold Legal Pendulum

```html
<!DOCTYPE html>
<html lang="en">
<head>
<meta charset="utf-8">
<title>TK Thekiso Incorporated – Stationery</title>
<link href="https://fonts.googleapis.com/css2?family=Open+Sans:wght@400;600;700&display=swap" rel="stylesheet">
<style>
  :root {
    --navy: #0b4470;
    --gold: #c9973f;
    --ink: #1d3f66;
    --grey: #8a8a8a;
    --page: #ffffff;
    --haze: #f1f1f1;
    --shadow: rgba(0,0,0,0.28);
  }
  * { margin: 0; padding: 0; box-sizing: border-box; }
  html, body { width: 1200px; height: 2224px; overflow: hidden; }
  body {
    position: relative;
    background: var(--page);
    font-family: "Open Sans", Arial, sans-serif;
    color: var(--navy);
  }
  .hero {
    position: absolute; left: 0; top: 0; width: 1200px; height: 587px;
    background: radial-gradient(ellipse at 50% 40%, #ffffff 0%, #fafafa 55%, var(--haze) 100%);
  }

  /* Firm name placeholder: one colour, one weight, one size, one plain circle */
  .brand {
    position: absolute; display: flex; align-items: center;
    font-weight: 600; color: var(--navy);
  }
  .brand__mark { flex: none; border-radius: 50%; background: var(--gold); }
  .brand__name { display: flex; flex-direction: column; line-height: 1.18; letter-spacing: 0.02em; }
  .brand--hero { left: 450px; top: 170px; width: 427px; gap: 22px; }
  .brand--hero .brand__mark { width: 60px; height: 60px; }
  .brand--hero .brand__name { font-size: 44px; }
  .brand--card { left: 69px; top: 152px; width: 231px; gap: 12px; }
  .brand--card .brand__mark { width: 30px; height: 30px; }
  .brand--card .brand__name { font-size: 22px; }
  .card--back .brand { left: 133px; top: 310px; color: #fff; }

  .hero__blurb {
    position: absolute; left: 230px; top: 488px; width: 740px;
    text-align: center; font-size: 15px; line-height: 1.3; color: var(--grey);
  }
  .address {
    position: absolute; left: 928px; top: 640px; display: flex; gap: 12px; align-items: flex-start;
    font-size: 19px; line-height: 1.05; color: #555; letter-spacing: 0.06em;
  }
  .card { position: absolute; width: 457px; height: 764px; }
  .card--back {
    left: 591px; top: 1153px; background: var(--navy);
    box-shadow: 14px 14px 14px var(--shadow);
  }
  .card--front {
    left: 162px; top: 967px; background: var(--page);
    box-shadow: 10px 10px 0 #d4d4d4, 20px 20px 0 #bcbcbc, 26px 28px 22px var(--shadow);
  }
  .card__name { position: absolute; left: 86px; top: 411px; font-size: 34px; font-weight: 700; line-height: 1; }
  .card__role { position: absolute; left: 86px; top: 454px; font-size: 23px; line-height: 1; }
  .card__details {
    position: absolute; left: 94px; top: 512px; font-size: 20.5px; line-height: 31.3px; list-style: none;
  }
  .card__icons { position: absolute; left: 56px; top: 553px; display: flex; flex-direction: column; gap: 12px; }
  .icon { width: 26px; height: 26px; display: block; flex: none; }
  .contacts {
    position: absolute; left: 48px; top: 1998px; list-style: none;
    display: flex; flex-direction: column; gap: 13px;
  }
  .contacts li { display: flex; align-items: center; gap: 16px; font-size: 19px; color: var(--ink); line-height: 26px; }
  .footer {
    position: absolute; left: 0; top: 2134px; width: 1200px; height: 90px;
    background: var(--navy); color: #fff; display: flex; align-items: center; justify-content: center;
    font-size: 21px;
  }
</style>
</head>
<body>
  <section class="hero">
    <div class="brand brand--hero">
      <span class="brand__mark"></span>
      <span class="brand__name"><span>TK</span><span>THEKISO</span><span>INCORPORATED</span></span>
    </div>
    <p class="hero__blurb">Lorem Ipsum is simply dummy text of the printing and typesetting industry. Lorem Ipsum has been the industry's stawhen an unknown printer took a galley of type and scrambled it to make a type specimen book.electronic</p>
  </section>

  <div class="address">
    <svg class="icon" viewBox="0 0 24 24" aria-hidden="true"><path d="M12 2a7 7 0 0 0-7 7c0 5 7 13 7 13s7-8 7-13a7 7 0 0 0-7-7z" fill="#8d8d8d"/><circle cx="12" cy="9" r="3" fill="#fff"/></svg>
    <span>P O Box 00 .adress<br>and00demoadress</span>
  </div>

  <div class="card card--back">
    <div class="brand brand--card">
      <span class="brand__mark"></span>
      <span class="brand__name"><span>TK</span><span>THEKISO</span><span>INCORPORATED</span></span>
    </div>
  </div>

  <div class="card card--front">
    <div class="brand brand--card">
      <span class="brand__mark"></span>
      <span class="brand__name"><span>TK</span><span>THEKISO</span><span>INCORPORATED</span></span>
    </div>
    <p class="card__name">NAME</p>
    <p class="card__role">Director</p>
    <div class="card__icons">
      <svg class="icon" viewBox="0 0 24 24" aria-hidden="true"><circle cx="12" cy="12" r="12" fill="var(--navy)"/><path d="M8 6l2 0 1 3-1.5 1a7 7 0 0 0 3.5 3.5l1-1.5 3 1 0 2c0 1-1 2-2 2A10 10 0 0 1 6 8c0-1 1-2 2-2z" fill="#fff"/></svg>
      <svg class="icon" viewBox="0 0 24 24" aria-hidden="true"><circle cx="12" cy="12" r="12" fill="var(--navy)"/><rect x="6" y="8" width="12" height="8" fill="#fff"/><path d="M6 8l6 5 6-5" stroke="var(--navy)" stroke-width="1.3" fill="none"/></svg>
      <svg class="icon" viewBox="0 0 24 24" aria-hidden="true"><circle cx="12" cy="12" r="12" fill="var(--navy)"/><circle cx="12" cy="12" r="6" stroke="#fff" stroke-width="1.4" fill="none"/><path d="M6 12h12M12 6c-3 3-3 9 0 12M12 6c3 3 3 9 0 12" stroke="#fff" stroke-width="1.2" fill="none"/></svg>
    </div>
    <ul class="card__details">
      <li>Block C Riverbend Office Park</li>
      <li>42 Acacia road north</li>
      <li>Northview 2190</li>
      <li>Tel: 011 555 0187</li>
      <li>Fax: 086 555 0142</li>
      <li>info@tkthekiso.co.za</li>
    </ul>
  </div>

  <ul class="contacts">
    <li><svg class="icon" viewBox="0 0 24 24" aria-hidden="true"><circle cx="12" cy="12" r="12" fill="var(--navy)"/><path d="M8 6l2 0 1 3-1.5 1a7 7 0 0 0 3.5 3.5l1-1.5 3 1 0 2c0 1-1 2-2 2A10 10 0 0 1 6 8c0-1 1-2 2-2z" fill="#fff"/></svg>+00(0) 123 456 789</li>
    <li><svg class="icon" viewBox="0 0 24 24" aria-hidden="true"><circle cx="12" cy="12" r="12" fill="var(--navy)"/><rect x="6" y="8" width="12" height="8" fill="#fff"/><path d="M6 8l6 5 6-5" stroke="var(--navy)" stroke-width="1.3" fill="none"/></svg>ABC@ABCDE.COM</li>
    <li><svg class="icon" viewBox="0 0 24 24" aria-hidden="true"><circle cx="12" cy="12" r="12" fill="var(--navy)"/><circle cx="12" cy="12" r="6" stroke="#fff" stroke-width="1.4" fill="none"/><path d="M6 12h12M12 6c-3 3-3 9 0 12M12 6c3 3 3 9 0 12" stroke="#fff" stroke-width="1.2" fill="none"/></svg>WWW.BCDE.COM</li>
  </ul>

  <footer class="footer">Director: Tumelo Kagiso Thekiso BA, LLB and HDip Tax Law</footer>
</body>
</html>
```